Event Center Website

We need a new website design for an upscale event center in Reno, Nevada. The building hosts everything from weddings to corporate events to funerals and it competitively more expensive. The overall look and feel is consistent with a Lake Tahoe aesthetic. The current site can be viewed at www.maplehallvenue.com. They are looking for a major upgrade. A sample site they like is www.cedarbluffstay.com. We have new photography available (some attached). The site should be very visual. A site map is attached as well for direction on what elements the site should include as well as labels for navigation. I am looking for a home page and sample interior page. Any questions, let me know. Thanks.
Updates

I have added some photography of the center itself for use rather than stock photography. Thanks!

Target Market(s)

Brides, professionals, high-income

Industry/Entity Type

Building

Requirements
Must have
• See site map

```html
<!DOCTYPE html>
<html lang="en">
<head>
<meta charset="utf-8">
<title>Maple Hall at Cedar Creek</title>
<link rel="stylesheet" href="https://fonts.googleapis.com/css2?family=Oswald:wght@300;400&family=Open+Sans:wght@400&display=swap">
<style>
  :root {
    --brown: #5a3418;
    --brown-dark: #3e2210;
    --cream: #f3ead3;
    --cream-edge: #e7dcc0;
    --white: #ffffff;
    --ink: #4a4a4a;
    --heading: #3c3c3c;
    --footer: #120202;
    --footer-text: #b9b2aa;
    --field-line: #e2dccd;
    --field-text: #8a8a8a;
  }
  * { margin: 0; padding: 0; box-sizing: border-box; }
  html, body { width: 1200px; height: 968px; overflow: hidden; background: var(--white); }
  body { position: relative; font-family: "Open Sans", sans-serif; }

  .hero {
    position: absolute; left: 0; top: 0; width: 1200px; height: 682px;
    background:
      linear-gradient(180deg, rgba(0,0,0,0) 55%, rgba(70,50,30,.35) 100%),
      radial-gradient(ellipse 420px 330px at 560px 440px, #8a5a34 0%, #6b4a30 45%, rgba(107,74,48,0) 100%),
      linear-gradient(180deg, #2a5aa8 0%, #3f78c0 35%, #6d8fb4 55%, #5a6848 72%, #4d5a3c 88%, #7d7a70 100%);
  }
  .hero-arrow {
    position: absolute; top: 385px; width: 40px; height: 40px; border-radius: 50%;
    background: rgba(40,40,40,.55);
  }
  .hero-arrow svg { position: absolute; left: 12px; top: 11px; }
  .hero-arrow.prev { left: 38px; }
  .hero-arrow.next { left: 1118px; }

  .site-header { position: absolute; left: 0; top: 0; width: 1200px; height: 100px; }
  .brand {
    position: absolute; left: 98px; top: 27px; width: 173px; height: 56px;
    background: var(--brown); display: flex; align-items: center; justify-content: center;
    font-family: "Oswald", sans-serif; font-weight: 400; font-size: 22px; color: var(--white);
    letter-spacing: .5px;
  }
  .main-nav {
    position: absolute; left: 346px; top: 41px; width: 755px;
    display: flex; justify-content: space-between;
  }
  .main-nav a {
    font-family: "Oswald", sans-serif; font-weight: 300; font-size: 15px;
    color: var(--white); text-decoration: none; letter-spacing: -.2px; line-height: 24px;
  }

  .booking {
    position: absolute; left: 99px; top: 653px; width: 1003px; height: 94px;
    background: var(--cream); border: 1px solid var(--cream-edge); border-radius: 3px;
    box-shadow: 0 10px 10px -6px rgba(0,0,0,.35);
  }
  .booking-title {
    position: absolute; left: 18px; top: 30px;
    font-family: "Oswald", sans-serif; font-weight: 300; font-size: 20px; color: var(--brown-dark);
  }
  .field {
    position: absolute; top: 24px; width: 182px; height: 41px;
    background: var(--white); border: 1px solid var(--field-line); border-radius: 2px;
    font-size: 12.5px; color: var(--field-text); line-height: 39px; padding-left: 12px;
  }
  .field svg { position: absolute; right: 12px; top: 14px; }
  .field.arrival { left: 218px; }
  .field.departure { left: 415px; }
  .field.adults { left: 612px; }
  .reserve {
    position: absolute; left: 802px; top: 24px; width: 182px; height: 41px;
    background: var(--brown); border-radius: 2px; color: var(--white);
    font-family: "Oswald", sans-serif; font-weight: 300; font-size: 15px;
    text-align: center; line-height: 41px;
  }

  .welcome { position: absolute; left: 0; top: 762px; width: 1200px; text-align: center; }
  .welcome h1 {
    font-family: "Oswald", sans-serif; font-weight: 300; font-size: 30px; color: var(--heading);
    line-height: 44px;
  }
  .welcome p {
    width: 870px; margin: 9px auto 0; font-size: 12.5px; line-height: 20.6px; color: var(--ink);
  }

  .site-footer {
    position: absolute; left: 0; top: 905px; width: 1200px; height: 63px; background: var(--footer);
    font-family: "Oswald", sans-serif; font-weight: 300; font-size: 12px; color: var(--footer-text);
  }
  .copyright { position: absolute; left: 99px; top: 22px; }
  .social { position: absolute; left: 518px; top: 16px; display: flex; gap: 5px; }
  .social span {
    width: 29px; height: 29px; border-radius: 50%; border: 1.5px solid var(--footer-text);
  }
  .legal { position: absolute; right: 99px; top: 22px; }
</style>
</head>
<body>
  <div class="hero" role="img" aria-label="Photo of the timber-frame event center entrance under a blue sky with gardens in front"></div>
  <div class="hero-arrow prev"><svg width="14" height="18" viewBox="0 0 14 18"><path d="M10 2 L3 9 L10 16" fill="none" stroke="#fff" stroke-width="2.2"/></svg></div>
  <div class="hero-arrow next"><svg width="14" height="18" viewBox="0 0 14 18"><path d="M4 2 L11 9 L4 16" fill="none" stroke="#fff" stroke-width="2.2"/></svg></div>

  <header class="site-header">
    <div class="brand">Maple Hall</div>
    <nav class="main-nav">
      <a href="#">ABOUT US</a><a href="#">GALLERY</a><a href="#">WEDDINGS</a><a href="#">MEETINGS</a>
      <a href="#">OTHER EVENTS</a><a href="#">CATERING</a><a href="#">MENUS</a><a href="#">FAQS</a>
      <a href="#">TESTIMONIALS</a><a href="#">CONTACT</a>
    </nav>
  </header>

  <section class="booking">
    <div class="booking-title">Schedule an Appointment</div>
    <div class="field arrival">Arrival Date<svg width="12" height="12" viewBox="0 0 12 12"><rect x="0.5" y="1.5" width="11" height="10" fill="none" stroke="#999"/><path d="M0.5 4h11M4 4v7.5M8 4v7.5M0.5 7.5h11" stroke="#999" stroke-width="0.8"/></svg></div>
    <div class="field departure">Departure Date<svg width="12" height="12" viewBox="0 0 12 12"><rect x="0.5" y="1.5" width="11" height="10" fill="none" stroke="#999"/><path d="M0.5 4h11M4 4v7.5M8 4v7.5M0.5 7.5h11" stroke="#999" stroke-width="0.8"/></svg></div>
    <div class="field adults">Adults<svg width="12" height="12" viewBox="0 0 12 12"><rect x="0.5" y="1.5" width="11" height="10" fill="none" stroke="#999"/><path d="M0.5 4h11M4 4v7.5M8 4v7.5M0.5 7.5h11" stroke="#999" stroke-width="0.8"/></svg></div>
    <div class="reserve">RESERVE Online</div>
  </section>

  <section class="welcome">
    <h1>Welcome To Maple Hall</h1>
    <p>Maple Hall is an 8,000 square foot dedicated special events center facility with a full kitchen, bar, and outdoor patio. Maple Hall provides the ideal venue for weddings, business meetings, or any other special event. We have a full time kitchen staff and on site planning staff to assist you with all your catering and event planning needs. We offer a unique and private setting to host your event. From the latest audio and visual</p>
  </section>

  <footer class="site-footer">
    <div class="copyright">©2013 - 2014&nbsp; Maple Hall at Cedar Creek , All Rights Reserved.</div>
    <div class="social"><span></span><span></span><span></span><span></span><span></span></div>
    <div class="legal">PRIVACY POLICY&nbsp; / &nbsp;CAREERS</div>
  </footer>
</body>
</html>
```